New Business Card Design Project

Make a kick ass business card for The Otter Tea Mug, using the designs. I also might like the 2nd place design logo on the back? Maybe all black with that? Not sure. Also, I'm cool with it being on metal, plastic, glass? or whatever for the business card. Maybe shaped like a shark? Let me know what else you need? Would like designs in the next day or so. Thank you.
Target Market(s)
Anyone that is cool
Contact Information for Business Card
Name: Dorian Fenwick
Phone: 317.594.8126
inventor/creator/entrepreneur/owner
www.theottertyeamug.example
social media links
https://www.facebook.com/theottertyeamug
https://twitter.com/otter_brew
https://www.instagram.com/theottertyeamug/
I'll get the Pinterest one soon
Colors
Designer to choose colors to be used in the design.
Requirements
Must have
- The Otter Tea Mug
- www.theottertyeamug.example
- social media tags?
- My logos and picture/photo of wine glass
Nice to have
- Maybe shaped like a wine glass or shark
- I'll let you decide but my same colors from my website would be nice

```html
<!DOCTYPE html>
<html lang="en">
<head>
<meta charset="utf-8">
<title>The Otter Tea Mug – Business Card</title>
<link href="https://fonts.googleapis.com/css2?family=Montserrat:wght@400;500;600;700&display=swap" rel="stylesheet">
<style>
  :root {
    --brand-red: #b8434a;
    --brand-red-soft: #cf6a70;
    --brand-red-pale: #f1d3d4;
    --ink-grey: #6b6b6b;
    --paper: #ffffff;
    --backdrop: #f6ece9;
  }
  * { box-sizing: border-box; margin: 0; padding: 0; }
  html, body {
    width: 1200px; height: 1200px; overflow: hidden;
    background: var(--backdrop);
  }
  .sheet {
    width: 1200px; height: 1200px;
    display: flex; flex-direction: column; align-items: center; justify-content: center;
    gap: 42px;
  }
  .card {
    position: relative; width: 940px; height: 537px; overflow: hidden;
    background: var(--paper);
    box-shadow: 0 6px 18px rgba(120, 60, 60, 0.18);
  }

  /* Front */
  .front .wave-band {
    position: absolute; left: 0; width: 100%;
    background: var(--brand-red);
  }
  .front .wave-band.top { top: 0; height: 96px; border-radius: 0 0 40% 40% / 0 0 60px 60px; }
  .front .wave-band.bottom { bottom: 0; height: 112px; border-radius: 40% 40% 0 0 / 60px 60px 0 0; }
  .front .brand-name {
    position: absolute; left: 0; right: 0; top: 236px;
    display: flex; align-items: center; justify-content: center; gap: 18px;
    font-family: "Montserrat", sans-serif; font-weight: 500;
    font-size: 40px; line-height: 1; color: var(--ink-grey); letter-spacing: 1px;
  }
  .brand-dot {
    width: 30px; height: 30px; border-radius: 50%;
    background: var(--brand-red); flex: none;
  }

  /* Back */
  .back .glass-side {
    position: absolute; left: 0; top: 0; width: 403px; height: 100%;
    background: var(--paper);
  }
  .back .glass-art {
    position: absolute; left: 30px; top: 16px; width: 340px; height: 521px;
    background: linear-gradient(180deg, var(--brand-red-pale), #e9b6b9);
    border-radius: 0 0 170px 170px / 0 0 220px 220px;
  }
  .back .glass-side .brand-name {
    position: absolute; left: 0; width: 403px; top: 200px;
    text-align: center;
    font-family: "Montserrat", sans-serif; font-weight: 500;
    font-size: 26px; line-height: 1; color: var(--ink-grey); letter-spacing: 0.5px;
  }
  .back .info-side {
    position: absolute; left: 403px; top: 0; right: 0; height: 100%;
    background: var(--brand-red); color: var(--paper);
  }
  .back .name {
    position: absolute; left: 0; right: 0; top: 44px;
    text-align: center;
    font-family: "Montserrat", sans-serif; font-weight: 700;
    font-size: 47px; letter-spacing: 0.5px; line-height: 1;
  }
  .back .role {
    position: absolute; left: 0; right: 0; top: 100px;
    text-align: center;
    font-family: "Montserrat", sans-serif; font-weight: 400;
    font-size: 19px; letter-spacing: 0.3px;
  }
  .back .contacts {
    position: absolute; left: 40px; top: 186px; list-style: none;
  }
  .back .contacts li {
    display: flex; align-items: center; gap: 22px;
    height: 51px;
    font-family: "Montserrat", sans-serif; font-weight: 500;
    font-size: 21px; letter-spacing: 0.4px;
  }
  .back .icon { width: 28px; height: 28px; flex: none; display: flex; align-items: center; justify-content: center; }
  .back .icon .dot { width: 20px; height: 20px; border-radius: 50%; background: var(--paper); }
  .back .mini-glass {
    position: absolute; right: 34px; top: 180px; width: 110px; height: 260px;
    background: linear-gradient(180deg, var(--brand-red-soft), #c4545a);
    border-radius: 0 0 55px 55px / 0 0 80px 80px;
  }
  .back .web-link {
    position: absolute; left: 98px; top: 488px; width: 372px; height: 36px;
    border: 1.5px solid var(--paper); border-radius: 7px;
    display: flex; align-items: center; justify-content: center;
    font-family: "Montserrat", sans-serif; font-weight: 400;
    font-size: 18px;
  }
</style>
</head>
<body>
<main class="sheet">

  <section class="card front" aria-label="Business card front">
    <div class="wave-band top" role="img" aria-label="Red curling wave ornament along the top edge"></div>
    <div class="brand-name"><span class="brand-dot" aria-hidden="true"></span>The Otter Tea Mug</div>
    <div class="wave-band bottom" role="img" aria-label="Red curling wave ornament along the bottom edge"></div>
  </section>

  <section class="card back" aria-label="Business card back">
    <div class="glass-side">
      <div class="glass-art" role="img" aria-label="Large red outline illustration of a glass framing the brand name"></div>
      <div class="brand-name">The Otter Tea Mug</div>
    </div>

    <div class="info-side">
      <h1 class="name">DORIAN FENWICK</h1>
      <p class="role">INVENTOR CREATOR ENTREPRENEUR OWNER</p>

      <ul class="contacts">
        <li>
          <span class="icon">
            <svg width="24" height="24" viewBox="0 0 24 24" aria-hidden="true">
              <path fill="#fff" d="M6.6 10.8a15.1 15.1 0 0 0 6.6 6.6l2.2-2.2c.3-.3.7-.4 1-.2 1.1.4 2.3.6 3.6.6.6 0 1 .4 1 1V20c0 .6-.4 1-1 1A17 17 0 0 1 3 4c0-.6.4-1 1-1h3.5c.6 0 1 .4 1 1 0 1.3.2 2.5.6 3.6.1.3 0 .7-.2 1z"/>
            </svg>
          </span>
          317-594-8126
        </li>
        <li><span class="icon"><span class="dot"></span></span>THEOTTERTYEAMUG</li>
        <li><span class="icon"><span class="dot"></span></span>OTTER_BREW</li>
        <li><span class="icon"><span class="dot"></span></span>THEOTTERTYEAMUG</li>
        <li><span class="icon"><span class="dot"></span></span>THEOTTERTYEAMUG</li>
      </ul>

      <div class="mini-glass" role="img" aria-label="Small white outline glass with the brand mark inside"></div>

      <div class="web-link">www.theottertyeamug.example</div>
    </div>
  </section>

</main>
</body>
</html>
```